customer services company for the travel industry needs a flyer designed

we need a flyer for our London based company. We are an outsource service to the travel industry so our client companies receive a complaint from their customer about their holiday or travel arrangements and they pass it to us to handle. We take the stress and strain away from them that complaints present! check out our website www.fernmoorassist.co.uk - blue features as our corporate colors. The business is 26 years old so well established in the industry. The reverse of the flyer will be printed with endorsements from current company clients. I would like something light hearted projecting the relief of pressure we can provide whilst also suggesting complaints and complainants will be in professional safe capable hands

Industry/Entity Type

Travel

```html
<!DOCTYPE html>
<html lang="en">
<head>
<meta charset="utf-8">
<title>Fernmoor Assist – Flyer</title>
<link rel="stylesheet" href="https://fonts.googleapis.com/css2?family=Quicksand:wght@400&family=Open+Sans:wght@400;600&family=Carlito:wght@400;700&display=swap">
<style>
  :root{
    --stage:#2f8ef0;
    --brand:#3a8fd8;
    --brand-strong:#2b8ae6;
    --tag-grey:#8a8f95;
    --teal-light:#7fe0ee;
    --teal-mid:#35b6cc;
    --teal-deep:#1f7f9d;
    --cyan-rule:#6fe3f2;
    --band-dark:#2b302f;
    --band-darker:#1c201f;
    --link-cyan:#7fe6f5;
    --ink:#111;
    --attrib:#2a84c4;
    --panel-1:#d3e7fa;
    --panel-2:#e4f0fb;
    --panel-3:#eef5fc;
    --panel-4:#f4f8fd;
  }
  *{box-sizing:border-box;margin:0;padding:0}
  html,body{width:1200px;height:1000px;overflow:hidden}
  body{background:var(--stage);position:relative;font-family:"Open Sans",sans-serif}

  .flyer{position:absolute;background:#fff;overflow:hidden;box-shadow:-14px 18px 28px rgba(0,0,50,.35)}
  .flyer--front{left:218px;top:87px;width:376px;height:828px}
  .flyer--back{left:706px;top:87px;width:378px;height:836px}

  .brand{position:absolute;left:0;right:0;top:28px;text-align:right;padding-right:12px}
  .brand__name{font-family:"Quicksand",sans-serif;font-weight:400;color:var(--brand);font-size:41px;line-height:44px;letter-spacing:-.3px}
  .brand__tagline{font-family:"Quicksand",sans-serif;color:var(--tag-grey);font-size:11px;margin-top:6px}

  /* front */
  .hero-photo{position:absolute;left:0;top:100px;width:376px;height:340px;
    background:linear-gradient(160deg,#f4f1e6 0%,#e7dcc2 35%,#d4c6a8 60%,#b7b5ad 100%)}
  .wave{position:absolute;left:0;top:400px;width:376px;height:60px}
  .info-panel{position:absolute;left:0;top:440px;width:376px;height:282px;
    background:linear-gradient(180deg,var(--teal-light) 0%,var(--teal-mid) 45%,var(--teal-deep) 100%)}
  .info-panel__copy{position:absolute;left:14px;top:26px;width:205px;color:#fff;font-size:14.2px;line-height:18.6px}
  .info-panel__copy p+p{margin-top:11px}
  .suitcase-art{position:absolute;left:232px;top:36px;width:118px;height:200px;border-radius:14px;
    background:linear-gradient(180deg,rgba(255,255,255,.45),rgba(150,235,250,.55))}
  .partners{position:absolute;right:14px;bottom:14px;display:flex;gap:8px}
  .partners span{display:block;width:38px;height:14px;background:rgba(255,255,255,.8);border-radius:2px}

  .cyan-rule{position:absolute;left:0;height:10px;width:100%;background:var(--cyan-rule)}
  .footer-band{position:absolute;left:0;bottom:0;width:100%;
    background:linear-gradient(180deg,var(--band-dark),var(--band-darker));color:#fff;text-align:center}
  .flyer--front .cyan-rule{top:722px}
  .flyer--front .footer-band{top:732px}
  .call__label{font-size:23px;margin-top:10px;line-height:28px}
  .call__phone{font-size:23px;line-height:30px}
  .web{color:var(--link-cyan);font-size:14px;margin-top:2px}

  /* back */
  .reputation__title{position:absolute;left:18px;top:120px;font-size:18.5px;font-weight:600;color:var(--ink);letter-spacing:.1px}
  .reputation__title strong{color:var(--brand-strong);font-weight:700}
  .testimonial{position:absolute;left:0;width:378px;padding:12px 14px 0 18px;font-family:"Carlito",sans-serif;font-size:13.6px;line-height:17px;color:var(--ink);border-top:1px solid #fff}
  .testimonial__who{color:var(--attrib)}
  .t1{top:149px;height:148px;background:linear-gradient(180deg,var(--panel-1),#e2effb)}
  .t2{top:297px;height:150px;background:linear-gradient(180deg,var(--panel-2),#f1f7fd)}
  .t3{top:447px;height:131px;background:linear-gradient(180deg,var(--panel-3),#f6f9fd)}
  .t4{top:578px;height:126px;background:linear-gradient(180deg,var(--panel-4),#fff)}
  .welcome{position:absolute;left:0;width:100%;top:710px;text-align:center;font-family:"Carlito",sans-serif;font-size:14px;color:var(--ink)}
  .flyer--back .cyan-rule{top:733px}
  .flyer--back .footer-band{top:743px}
  .address{font-family:"Carlito",sans-serif;font-size:12px;line-height:16px;color:#e8e8e8;margin-top:8px}
  .contact{font-family:"Carlito",sans-serif;font-size:12px;font-weight:700;margin-top:12px;word-spacing:1px}
  .contact span+span{margin-left:14px}
  .flyer--back .web{font-size:14px;margin-top:2px}
</style>
</head>
<body>

<section class="flyer flyer--front">
  <header class="brand">
    <div class="brand__name">Fernmoor Assist</div>
    <div class="brand__tagline">Customer Service &amp; Training Specialists</div>
  </header>

  <div class="hero-photo" role="img" aria-label="Photo of a smiling couple of tourists in sunglasses pointing and holding a map in a sunny old town street"></div>

  <svg class="wave" viewBox="0 0 376 60" preserveAspectRatio="none" aria-hidden="true">
    <path d="M0 30 C90 10 200 70 376 20 L376 60 L0 60 Z" fill="#8fe4f0"/>
    <path d="M0 40 C110 22 210 72 376 32 L376 60 L0 60 Z" fill="#2a9bbd"/>
    <path d="M0 46 C110 30 220 76 376 42 L376 60 L0 60 Z" fill="#7fe0ee"/>
  </svg>

  <div class="info-panel">
    <div class="info-panel__copy">
      <p>Our professional, experienced team manage customer service issues and complaints for travel companies serving the UK and Ireland markets.</p>
      <p>We work with tour operators, travel agents, bed banks, cruise lines, coach companies, airlines and dynamic packaging agents to help them manage and resolve their consumer complaints and claims.</p>
    </div>
    <div class="suitcase-art" role="img" aria-label="Illustration of a suitcase filled with small travel icons"></div>
    <div class="partners" aria-hidden="true"><span></span><span></span><span></span></div>
  </div>

  <div class="cyan-rule"></div>
  <footer class="footer-band">
    <div class="call__label">Call Us Now</div>
    <div class="call__phone">+44 20 7946 0321</div>
    <div class="web">www.fernmoorassist.co.uk</div>
  </footer>
</section>

<section class="flyer flyer--back">
  <header class="brand">
    <div class="brand__name">Fernmoor Assist</div>
    <div class="brand__tagline">Customer Service &amp; Training Specialists</div>
  </header>

  <h2 class="reputation__title">OUR HARD EARNED <strong>REPUTATION</strong></h2>

  <blockquote class="testimonial t1">
    ‘Our members have made use of and appreciated the knowledge and experience of the team at Fernmoor Assist over many years. The training courses provided by Sofia for GITP always receive very good reviews. ’
    <div class="testimonial__who">Maria Oakden<br>Partnership and Events Manager<br>Guild of Independent Tour Planners</div>
  </blockquote>

  <blockquote class="testimonial t2">
    'It is great to have the support of Janet and her colleagues when the going gets rough. Happily we do not have to call upon them often but we have received excellent service from them over the years when we have needed help. We are happy to endorse Fernmoor Assist.'
    <div class="testimonial__who">Clara Whitmore<br>Northern Steppe Journeys</div>
  </blockquote>

  <blockquote class="testimonial t3">
    'We have found the experience and knowledge of the team at Fernmoor Assist invaluable with the more complex claims that arise from time to time'.
    <div class="testimonial__who">Daniel Hart<br>Head of Customer Support<br>Wayfare Travel</div>
  </blockquote>

  <blockquote class="testimonial t4">
    'We have been delighted with the access we have to such knowledgeable and friendly support. I have no hesitation in recommending Fernmoor Assist.'
    <div class="testimonial__who">Rosa Penfold<br>Managing Director<br>Sunhaven Villas</div>
  </blockquote>

  <p class="welcome">We welcome enquiries from the travel trade industry.</p>

  <div class="cyan-rule"></div>
  <footer class="footer-band">
    <div class="address">Unit 22 Kestrel Yard 40-44 Harrow Lane<br>London&nbsp; N7 0QT</div>
    <div class="contact"><span>Tel: +44 20 7946 0321</span><span>Email: help@fernmoorassist.co.uk</span></div>
    <div class="web">www.fernmoorassist.co.uk</div>
  </footer>
</section>

</body>
</html>
```